Flyer-Design für Aufbereiter von Fahrzeugen
Zielgruppe
Wir reinigen und aufbereiten (polieren, versiegeln) Fahrzeuge, vorwiegend Autos. Zusätzlich leihen wir Personal an Autowerkstätten für Servicereinigungen und Fahrzeugaufbereitung an. Unsere Kunden sind Privatpersonen: Junge Autofan aus der Tuningszene und gutsituierte mit Luxusautos. Weitere Kunden sind Gewerbliche für professionelle Fahrzeugaufbereitung und Manpower ausleihen.
Hier finden Sie unsere Tätigkeiten https://www.glanzwerk-muster.ch/unsere-leistungen/
Aufgabenstellung
Mit diesem Flyer wollen wir im besonderen die private Kundschaft ansprechen: Fahrzeugreinigung und -aufbereitung mit Hightech-Ergebnis. Der Flyer, A4, legen wir 1x zusammen und in ein durchsichtiges Couvert C5, sodass von beiden Seiten der Flyer gelesen werden kann. Wir verteilen ihn meistens nach einem Gespräch an Interessierte. Auf der Rückseite der Visitenkarte steht bei uns "Treten Sie glänzend auf..." und auf dem TShirt steht seitlich "we clean your dream" leuchtgrün/gelb. Die Internetseite ist mal so eine Erstausgabe, welche wir in einem späteren Zeitpunkt auch nochmals updaten wollen.
Bei Verwendung von Foto Nr. 123122 bitte Uhr entfernen

```html
<!DOCTYPE html>
<html lang="de">
<head>
<meta charset="utf-8">
<title>Glanzwerk Muster – Fahrzeugaufbereitung</title>
<link href="https://fonts.googleapis.com/css2?family=Ubuntu:wght@300;400;500;700&display=swap" rel="stylesheet">
<style>
  :root {
    --green: #8cc63f;
    --green-deep: #5e9c1f;
    --green-bright: #a6d84a;
    --dark: #262626;
    --dark-soft: #353535;
    --white: #ffffff;
  }
  html, body { margin: 0; padding: 0; overflow: hidden; background: var(--dark); }
  .flyer {
    position: relative; width: 848px; height: 1200px; overflow: hidden;
    font-family: "Ubuntu", sans-serif; color: var(--white);
  }
  .backdrop { position: absolute; inset: 0; width: 848px; height: 1200px; }
  .brand {
    position: absolute; top: 500px; left: 0; width: 100%; text-align: center;
    font-size: 30px; font-weight: 400; color: var(--green); letter-spacing: 1px;
  }
  .brand-dot {
    display: inline-block; width: 12px; height: 12px; border-radius: 50%;
    background: var(--green); margin-right: 12px; vertical-align: middle;
  }
  .headline {
    position: absolute; top: 548px; left: 0; width: 100%; margin: 0; text-align: center;
    font-size: 53px; line-height: 60px; font-weight: 700; color: var(--green); letter-spacing: 1px;
  }
  .services {
    position: absolute; top: 716px; left: 0; width: 100%; margin: 0; padding: 0;
    list-style: none; text-align: center;
  }
  .services li {
    font-size: 29px; font-weight: 500; line-height: 46.5px; color: var(--green);
    letter-spacing: 0.5px;
  }
  .tick { width: 22px; height: 22px; vertical-align: -2px; margin-right: 6px; }
  .rule {
    position: absolute; top: 953px; left: 180px; width: 488px; height: 1px;
    background: linear-gradient(90deg, transparent, var(--green), transparent);
  }
  .website {
    position: absolute; top: 966px; left: 0; width: 100%; text-align: center;
    font-size: 44px; font-weight: 300; color: var(--white);
  }
  .contact {
    position: absolute; top: 1078px; left: 0; width: 100%; text-align: center;
    font-size: 19px; font-weight: 500; line-height: 27px; color: var(--white);
  }
  .contact .hours-title { font-size: 17px; line-height: 22px; }
</style>
</head>
<body>
<div class="flyer">
  <svg class="backdrop" viewBox="0 0 800 1132" preserveAspectRatio="none" aria-hidden="false">
    <defs>
      <linearGradient id="bg" x1="0" y1="0" x2="0" y2="1">
        <stop offset="0" stop-color="#7fba32"/>
        <stop offset="0.1" stop-color="#3a4a28"/>
        <stop offset="0.2" stop-color="#262626"/>
        <stop offset="0.82" stop-color="#2b2b2b"/>
        <stop offset="0.88" stop-color="#6fae2a"/>
        <stop offset="1" stop-color="#5e9c1f"/>
      </linearGradient>
      <linearGradient id="photo" x1="0" y1="0" x2="1" y2="1">
        <stop offset="0" stop-color="#8a8f93"/>
        <stop offset="0.5" stop-color="#3c3f42"/>
        <stop offset="1" stop-color="#1c1c1c"/>
      </linearGradient>
      <linearGradient id="swoosh" x1="0" y1="0" x2="1" y2="0">
        <stop offset="0" stop-color="#ffffff" stop-opacity="0.1"/>
        <stop offset="0.5" stop-color="#ffffff" stop-opacity="0.7"/>
        <stop offset="1" stop-color="#ffffff" stop-opacity="0.1"/>
      </linearGradient>
    </defs>
    <rect width="800" height="1132" fill="url(#bg)"/>
    <path d="M0 930 Q400 860 800 900 L800 1132 L0 1132 Z" fill="#3a3a3a" opacity="0.5"/>
    <path d="M0 985 Q400 915 800 955 L800 1132 L0 1132 Z" fill="#7cb92f"/>
    <path d="M0 960 Q400 900 800 935" fill="none" stroke="url(#swoosh)" stroke-width="3"/>
    <path d="M0 975 Q400 910 800 948" fill="none" stroke="url(#swoosh)" stroke-width="1.5"/>
    <path d="M0 1000 Q400 940 800 975 L800 1132 L0 1132 Z" fill="#6aa826"/>

    <g stroke="#8cc63f" stroke-width="5">
      <polygon role="img" aria-label="Foto: Hand im Handschuh poliert Karosserie mit Poliermaschine" points="90,112 235,257 90,402 -55,257" fill="url(#photo)"/>
      <polygon role="img" aria-label="Foto: Politur einer Autotür mit gelbem Polierpad" points="265,-30 398,103 265,236 132,103" fill="url(#photo)"/>
      <polygon role="img" aria-label="Foto: Innenreinigung der Mittelkonsole mit Pad" points="420,108 566,254 420,400 274,254" fill="url(#photo)"/>
      <polygon role="img" aria-label="Foto: Felgenreinigung mit Schaum und Schwamm" points="570,-32 710,108 570,248 430,108" fill="url(#photo)"/>
      <polygon role="img" aria-label="Foto: Mitarbeiter poliert Motorhaube mit Poliermaschine" points="712,110 858,256 712,402 566,256" fill="url(#photo)"/>
    </g>
  </svg>

  <div class="brand"><span class="brand-dot"></span>glanzwerk-muster.ch</div>

  <h1 class="headline">IHR AUTOGEREINIGT,<br>POLIERT &amp; VERSIEGELT</h1>

  <ul class="services">
    <li><svg class="tick" viewBox="0 0 22 22"><circle cx="11" cy="11" r="10" fill="#8cc63f"/><path d="M6 11.5 L9.5 15 L16 8" fill="none" stroke="#262626" stroke-width="2.6" stroke-linecap="round" stroke-linejoin="round"/></svg>FAHRZEUGWASCHE</li>
    <li><svg class="tick" viewBox="0 0 22 22"><circle cx="11" cy="11" r="10" fill="#8cc63f"/><path d="M6 11.5 L9.5 15 L16 8" fill="none" stroke="#262626" stroke-width="2.6" stroke-linecap="round" stroke-linejoin="round"/></svg>INNENREINIGUNG</li>
    <li><svg class="tick" viewBox="0 0 22 22"><circle cx="11" cy="11" r="10" fill="#8cc63f"/><path d="M6 11.5 L9.5 15 L16 8" fill="none" stroke="#262626" stroke-width="2.6" stroke-linecap="round" stroke-linejoin="round"/></svg>AUSSEN AUFBEREITUNG UND VERSIEGELUNG</li>
    <li><svg class="tick" viewBox="0 0 22 22"><circle cx="11" cy="11" r="10" fill="#8cc63f"/><path d="M6 11.5 L9.5 15 L16 8" fill="none" stroke="#262626" stroke-width="2.6" stroke-linecap="round" stroke-linejoin="round"/></svg>VERSIEGELUNG MIT GLANZ-&amp; SCHUTZWIRKUNG</li>
    <li><svg class="tick" viewBox="0 0 22 22"><circle cx="11" cy="11" r="10" fill="#8cc63f"/><path d="M6 11.5 L9.5 15 L16 8" fill="none" stroke="#262626" stroke-width="2.6" stroke-linecap="round" stroke-linejoin="round"/></svg>KONTROLLE - QUALITAT</li>
  </ul>

  <div class="rule"></div>
  <div class="website">www.glanzwerk-muster.ch</div>

  <div class="contact">
    Glanzwerk Muster GmbH – Werkstrasse 12 – 6330 Cham<br>
    Tel +41 (0)79 555 01 23 &nbsp;&nbsp; info@glanzwerk-muster.ch<br>
    <span class="hours-title">Öffnungszeiten</span><br>
    Mo 13:00 - 18:00 &nbsp;|&nbsp; Di bis Fr 09:00 - 18:00 h &nbsp;|&nbsp; Sa 09:00 - 12:00 h
  </div>
</div>
</body>
</html>
```